Velmora Capital, a private equity fund, needs a brochure

Velmora Capital is a private equity fund dedicated to the development of budget hotels in France (reasonably priced hotel rooms).
Our customers are French private and high-income investors.

The brochure should communicate :
- seriousness and expertise
- trust, confidence and security
- financial product and profitability

The title is : Investissez dans l'hôtellerie économique et l'immobilier

Brochure size :
3 pages A4
Open size : 63 x 29,7 cm
Closed size : 21 x 29,7 cm

Our competitors :
Trelundo http://trelundo-immo-exemple.fr/
789 Horizon http://www.789horizon-exemple.com/
RWL Capital http://www.rwlgx-exemple.com/
Sorvel capital http://www.sorvelcapital-exemple.fr/
Darmetis http://www.darmeto-exemple.fr/

Target Market(s)

Private investors, high-income ; Institutional investors ; Target customers are French private investors with high revenue.

Industry/Entity Type

Financial

Requirements
Must have
• - Brochure must respect our identity (you can see our logo) and use its colors and typo (and/or same typo style)
- You must use pictures on each interior pages (pictures of projetc and hotels)

```html
<!DOCTYPE html>
<html lang="fr">
<head>
<meta charset="utf-8">
<title>Velmora Capital – Trois sources potentielles de gains</title>
<link href="https://fonts.googleapis.com/css2?family=Tinos:wght@400;700&family=Ubuntu:wght@400;500&display=swap" rel="stylesheet">
<style>
  :root {
    --brand-red: #b00000;
    --text-red: #c00000;
    --page-grey: #dcdcdc;
    --page-light: #ececec;
    --sky: #5bc0f5;
    --azure: #3e8fd6;
    --navy: #1b5e96;
    --pale-blue: #c9e7f4;
    --wine: #9c4556;
    --year-grey: #c8dbe2;
    --ink: #5a3f4c;
    --white: #ffffff;
  }
  * { margin: 0; padding: 0; box-sizing: border-box; }
  html, body { width: 972px; height: 1200px; overflow: hidden; background: #f4f4f4; }
  .page {
    position: absolute; left: 72px; top: 16px;
    width: 827px; height: 1168px;
    background: linear-gradient(180deg, var(--page-light) 0%, var(--page-grey) 60%, #d6d6d6 100%);
    font-family: "Tinos", "Times New Roman", serif;
  }
  .photo-strip { position: absolute; left: 0; top: 0; width: 827px; height: 243px; display: flex; }
  .photo { height: 100%; }
  .photo--lounge { width: 278px; background: linear-gradient(135deg, #e9e2df 0%, #b8a3b4 45%, #6b2f6a 100%); }
  .photo--buffet { width: 318px; background: linear-gradient(160deg, #3a3a3a 0%, #8d8a7a 40%, #c9b48a 70%, #4d5a2f 100%); }
  .photo--atrium { width: 231px; background: linear-gradient(200deg, #f3f5f4 0%, #cdd5d2 50%, #7c8b7e 100%); }

  .gains-band {
    position: absolute; left: 12px; top: 243px; width: 806px; height: 314px;
    background: var(--brand-red); color: var(--white);
    padding: 10px 12px 0 10px;
  }
  .gains-title { font-size: 30px; font-weight: 400; line-height: 36px; margin-bottom: 8px; }
  .gains-intro { font-size: 11.4px; line-height: 13.8px; margin-bottom: 8px; }
  .gains-point { font-size: 14.8px; font-weight: 700; line-height: 23.5px; }
  .gains-summary { margin-top: 12px; font-size: 23px; font-weight: 700; line-height: 26px; }

  .timeline-card {
    position: absolute; left: 33px; top: 545px; width: 767px; height: 427px;
    background: var(--white); border: 3.5px solid var(--brand-red); border-radius: 22px;
    overflow: hidden;
  }
  .timeline-card svg { display: block; width: 100%; height: 100%; font-family: "Ubuntu", sans-serif; }

  .risk-note {
    position: absolute; left: 20px; top: 988px; width: 790px;
    color: var(--text-red); font-size: 17.6px; line-height: 20.8px;
  }
</style>
</head>
<body>
<main class="page">
  <div class="photo-strip">
    <div class="photo photo--lounge" role="img" aria-label="Salon d'hôtel aux canapés violets"></div>
    <div class="photo photo--buffet" role="img" aria-label="Buffet de petit-déjeuner d'hôtel"></div>
    <div class="photo photo--atrium" role="img" aria-label="Atrium moderne d'un hôtel avec plantes"></div>
  </div>

  <section class="gains-band">
    <h1 class="gains-title">Trois sources potentielles de gains :</h1>
    <p class="gains-intro">Une double plus-value potentielle hôtelière et immobilière assortie d’un rendement annuel. La création de valeur pour chacun des hôtels dans lesquels Velmora Capital prendra des participations proviendra de la valorisation des murs de l’hôtel, de la valorisation de son fonds de commerce et de la rentabilité annuelle de l’exploitation. L’activité de location de meublés de tourisme bénéficie des mêmes synergies.<br>La création de valeur pour l’activité de promotion immobilière (construction vente des immeubles) proviendra des marges dégagées par les opérations de promotion</p>
    <p class="gains-point">Trois sources potentielles de gains, assorties toutefois d’un risque de perte en capital</p>
    <p class="gains-point">Atténuation de risques du fait de l’investissement diversifié dans les murs et dans le fonds de commerce</p>
    <p class="gains-point">Un recours à un financement peu couteux</p>
    <p class="gains-summary">Plus-values hôtelières.<br>Plus-values immobilières.<br>Rendement annuel capitalisé.</p>
  </section>

  <section class="timeline-card">
    <svg viewBox="0 0 656 365" preserveAspectRatio="none" aria-label="Calendrier de l'investissement 2012 à 2019">
      <polygon points="15,208 412,18 412,208" fill="var(--pale-blue)"/>
      <line x1="15" y1="206" x2="408" y2="11" stroke="#c0506a" stroke-width="1.6"/>
      <polygon points="414,8 403,10 407,17" fill="#c0506a"/>
      <text x="306" y="157" text-anchor="middle" font-size="15" fill="var(--ink)">Espérance de gains</text>
      <text x="306" y="179" text-anchor="middle" font-size="15" fill="var(--ink)">pour l’investisseur</text>

      <rect x="419" y="19" width="181" height="59" fill="var(--sky)"/>
      <text x="509.5" y="53" text-anchor="middle" font-size="12" font-weight="500" fill="var(--white)">Plus values hôtelières</text>
      <rect x="419" y="84" width="181" height="58" fill="var(--azure)"/>
      <text x="509.5" y="117" text-anchor="middle" font-size="12" font-weight="500" fill="var(--white)">Plus values immobilières</text>
      <rect x="419" y="148" width="181" height="59" fill="var(--navy)"/>
      <text x="509.5" y="173" text-anchor="middle" font-size="12" font-weight="500" fill="var(--white)">Rendement annuel</text>
      <text x="509.5" y="190" text-anchor="middle" font-size="12" font-weight="500" fill="var(--white)">capitalisé</text>
      <rect x="606" y="19" width="35" height="188" fill="var(--pale-blue)"/>
      <text transform="translate(622 113) rotate(-90)" text-anchor="middle" font-size="11" fill="var(--ink)">Exonération fiscale</text>
      <text transform="translate(635 113) rotate(-90)" text-anchor="middle" font-size="7.5" fill="var(--ink)">(hors prélèvements sociaux)</text>

      <line x1="15" y1="212" x2="647" y2="212" stroke="#111" stroke-width="2"/>
      <rect x="15" y="218" width="181" height="58" fill="var(--wine)"/>
      <text x="105.5" y="252" text-anchor="middle" font-size="12" font-weight="500" fill="var(--white)">Investissements</text>
      <rect x="419" y="218" width="228" height="58" fill="var(--wine)"/>
      <text x="533" y="243" text-anchor="middle" font-size="12" font-weight="500" fill="var(--white)">Remboursement</text>
      <text x="533" y="260" text-anchor="middle" font-size="12" font-weight="500" fill="var(--white)">du capital initial</text>

      <line x1="15" y1="280" x2="647" y2="280" stroke="#111" stroke-width="1.4"/>
      <g stroke="#111" stroke-width="1.4">
        <line x1="49" y1="280" x2="49" y2="296"/>
        <line x1="108" y1="280" x2="108" y2="296"/>
        <line x1="172" y1="280" x2="172" y2="296"/>
        <line x1="287" y1="280" x2="287" y2="298"/>
        <line x1="420" y1="280" x2="420" y2="296"/>
      </g>
      <g fill="var(--year-grey)">
        <rect x="20" y="298" width="54" height="28"/>
        <rect x="84" y="298" width="54" height="28"/>
        <rect x="148" y="298" width="54" height="28"/>
        <rect x="260" y="298" width="54" height="28"/>
        <rect x="394" y="298" width="54" height="28"/>
      </g>
      <g font-size="16" fill="#222" text-anchor="middle">
        <text x="47" y="318">2012</text>
        <text x="111" y="318">2013</text>
        <text x="175" y="318">2014</text>
        <text x="287" y="318">2017</text>
        <text x="421" y="318">2019</text>
      </g>
      <text x="287" y="343" text-anchor="middle" font-size="11" font-weight="500" fill="#8b2a3a">Possibilité</text>
      <text x="287" y="360" text-anchor="middle" font-size="11" font-weight="500" fill="#8b2a3a">de sortie</text>
    </svg>
  </section>

  <p class="risk-note">L’attention des investisseurs est toutefois attirée sur l’impact de l’effet "moyenne" d’un tel affichage, lequel peut masquer de mauvais résultats pour certains fonds en particulier et lequel ne préjuge pas de performances d’un niveau équivalent pour le présent fond (étant en toutes hypothèses rappelé que Velmora Capital présente un risque de perte en capital). Par ailleurs, l’attention des investisseurs est attirée sur les facteurs de risques liés à un investissement dans Velmora Capital présentés ci-après dans le présent document<br>Des emplacements exceptionnels (centres villes, aéroports, zones commerciales).</p>
</main>
</body>
</html>
```